LOLU Baby Massage Classes - flyer to make a difference

I need a single page flyer, preferably single page, to hand out to doctors, medical centres and parents. To also leave on counters of establishments.
It is to promote my baby massage classes. Mums can get together with other mums and book a 5 week course to learn and discover the many benefits of baby massage.
Benefits include: enhances bonding and attachment, understand non-verbal cues from your baby, helps with sleep patterns, help with immune system, increases vagal activity,relief from wind, colic or constipation to name some.

Baby age from birth to 12 months. Group classes or private sessions

I am a Professional Member and Certified by the Global Society of Newborn Touch (GSNT) GSNT Australia is Nationally Accredited and is endorsed by Crown Academy of Carers, the Southern Guild of Birth Attendants, The Southern Union of Daily Living Therapy Australia, The Southern Union of Bodywork Practitioner and is a full member of Wellmind Network Australia.

Class detail and availability contact is Petra Holm 0487 315 208 petra.joanne.holm@quillmail.example www.lolunewborntouch com.au facebook/comLOLUnewborntouch

My colour scheme is green and purple as you will see from my logo and website. I would like my flyer to be softer tones of either both colours or just one.

I will include some images you can choose from or show me any you think will fit in with baby massage. THANK YOU
Updates

Hi The size of my flyer is A6. Approx 150mms x 210mms and single sided. Thank you

Target Market(s)

mums and dads, groups, doctors, midwives

Industry/Entity Type

Medical

Font styles to use
Sans Serif

Colors
87d0c7
b09cc8

Requirements
Must have
• baby photo or photos, both my logo and the GSNT logo. The GSNT logo is to be small
• Baby Massage Classes (wording) is very important to catch the eye.
• Invitation to book a class or gather friends to book is next in importance
• Benefits is next
• The admin information ie.,membership, certification and endorsements are lesser and can be small.
• Contact information to be noticeable.
Nice to have
• If you have an idea, drawing or photo that would look better, please feel free to try it
Should not have
• should not be crowded with information all the same size

```html
<!DOCTYPE html>
<html lang="en">
<head>
<meta charset="utf-8">
<title>LOLU Baby Massage Classes</title>
<link rel="stylesheet" href="https://fonts.googleapis.com/css2?family=Raleway:ital,wght@0,200;0,300;0,400;0,600;0,700;1,400;1,600&display=swap">
<style>
:root{
  --teal:#5e9f97;
  --teal-deep:#3f7f78;
  --teal-soft:#87d0c7;
  --purple:#8d5fb0;
  --purple-soft:#b09cc8;
  --green:#8cc63f;
  --white:#ffffff;
  --ink:#4a4a4a;
}
*{box-sizing:border-box;margin:0;padding:0}
html,body{width:849px;height:1200px;overflow:hidden;background:#fff}
body{font-family:'Raleway',sans-serif}
.flyer{position:relative;width:849px;height:1200px;overflow:hidden;background:var(--white)}
.backdrop{position:absolute;left:0;top:230px;width:849px;height:970px;
  background:linear-gradient(180deg,#79b7ae 0%,var(--teal) 35%,var(--teal-deep) 100%)}
.swooshes{position:absolute;left:0;top:0;width:849px;height:420px}
.brand{position:absolute;left:40px;top:30px;display:flex;align-items:center;gap:14px}
.brand-dot{width:70px;height:70px;border-radius:50%;background:var(--teal-soft)}
.brand-name{font-weight:700;font-size:52px;color:var(--purple);letter-spacing:2px}
.partner{position:absolute;left:660px;top:28px;font-weight:700;font-size:30px;color:var(--purple);letter-spacing:1px}
.portrait{position:absolute;left:585px;top:118px;width:150px;height:150px;border-radius:50%;
  border:6px solid var(--white);background:radial-gradient(circle at 50% 40%,#d9d4cf,#9b928c)}
.invite{position:absolute;left:20px;top:160px;width:190px;height:190px;border-radius:50%;
  background:var(--purple);color:var(--white);display:flex;align-items:center;justify-content:center;
  text-align:center;font-style:italic;font-weight:600;font-size:25px;line-height:1.2;padding:18px;z-index:3}
.baby-photo{position:absolute;left:90px;top:370px;width:370px;height:295px;background:var(--white);
  padding:12px;transform:rotate(-5deg);box-shadow:0 4px 14px rgba(0,0,0,.25);z-index:2}
.baby-photo div{width:100%;height:100%;background:linear-gradient(135deg,#f1e3da,#d8c2b6 60%,#bfa89c)}
.host-name{position:absolute;left:530px;top:272px;font-style:italic;font-weight:600;font-size:24px;color:var(--green)}
.host-bio{position:absolute;left:475px;top:310px;width:355px;font-size:16.5px;line-height:1.42;color:var(--white)}
.benefits{position:absolute;left:0;top:720px;width:849px;text-align:center;color:var(--white)}
.benefits h2{display:flex;align-items:center;justify-content:center;gap:22px;font-weight:300;font-size:34px;letter-spacing:1px}
.benefits h2::before,.benefits h2::after{content:"";width:160px;height:2px;background:var(--white)}
.benefits p{margin:14px auto 0;width:760px;font-size:20px;line-height:1.35;font-weight:400}
.headline{position:absolute;left:30px;top:930px;color:var(--white);font-weight:200}
.headline .big{display:block;font-size:150px;line-height:1;letter-spacing:4px}
.headline .sub{display:block;font-size:44px;letter-spacing:2px;margin-top:22px}
.contact{position:absolute;left:490px;top:940px;width:359px}
.phone{background:var(--green);color:var(--white);font-weight:700;font-size:44px;padding:12px 20px;letter-spacing:1px}
.line{display:block;margin-top:12px;background:var(--white);padding:9px 20px;font-size:18px;font-style:italic}
.line.email{color:var(--purple)}
.line.web{background:var(--purple);color:var(--white)}
.line.social{color:var(--purple)}
</style>
</head>
<body>
<main class="flyer">
  <div class="backdrop" role="img" aria-label="Soft faded photo of babies during a massage class"></div>
  <svg class="swooshes" viewBox="0 0 849 420" aria-hidden="true">
    <path d="M0 260 C200 200 420 220 600 160 C720 120 800 70 849 40 L849 0 L0 0 Z" fill="#ffffff"/>
    <path d="M0 240 C220 170 420 210 620 140 C730 100 800 60 849 30 L849 80 C780 120 700 180 600 210 C420 260 200 230 0 290 Z" fill="var(--green)"/>
    <path d="M0 180 C200 130 420 160 620 100 C720 70 800 40 849 20 L849 40 C780 80 690 130 600 150 C420 200 200 170 0 230 Z" fill="var(--purple)"/>
  </svg>
  <div class="brand"><span class="brand-dot"></span><span class="brand-name">LOLU</span></div>
  <div class="partner">GSNT</div>
  <div class="portrait" role="img" aria-label="Portrait photo of the instructor"></div>
  <div class="invite">book a class or gather friends to book</div>
  <figure class="baby-photo"><div role="img" aria-label="Photo of a baby receiving a gentle tummy massage"></div></figure>
  <p class="host-name">Petra Holm</p>
  <p class="host-bio">I am a Professional Member and Certified by the Global Society of Newborn Touch (GSNT) GSNT Australia is Nationally Accredited and is endorsed by Crown Academy of Carers, the Southern Guild of Birth Attendants, The Southern Union of Daily Living Therapy Australia, The Southern Union of Bodywork Practitioner and is a full member of Wellmind Network Australia.</p>
  <section class="benefits">
    <h2>BENEFITS INCLUDE:</h2>
    <p>enhances bonding and attachment, understand non-verbal cues from your baby, helps with sleep patterns, help with immune system, increases vagal activity,relief from wind, colic or constipation to name some.</p>
  </section>
  <h1 class="headline"><span class="big">BABY</span><span class="sub">MASSAGE CLASSES</span></h1>
  <address class="contact">
    <div class="phone">0487 315 208</div>
    <span class="line email">petra.joanne.holm@quillmail.example</span>
    <span class="line web">www.lolunewborntouch com.au</span>
    <span class="line social">facebook/comLOLUnewborntouch</span>
  </address>
</main>
</body>
</html>
```